We were billed for this because the project timed out. Please give me another designed to open this back up. I was not happy with the last designs (that I was charged for).
we are also using the logo with Clear Water Care From Every Angle
Also want to utilize Where Healthy Water is our Commitment.

Contact Information for Business Card

Marlowe Crest Group Inc

```html
<!DOCTYPE html>
<html lang="en">
<head>
<meta charset="utf-8">
<title>Marlowe Crest Group – Business Card</title>
<link href="https://fonts.googleapis.com/css2?family=Montserrat:wght@400;600;700;800&display=swap" rel="stylesheet">
<style>
  :root {
    --backdrop: #b3b3b3;
    --paper: #ffffff;
    --ink: #333333;
    --brand-blue: #1466b0;
    --brand-deep: #0d5ca6;
    --brand-light: #3d95d6;
    --back-top: #1769b2;
    --back-bottom: #3f97d5;
    --back-mark: #1a5e9e;
  }
  html, body {
    margin: 0;
    padding: 0;
    width: 1200px;
    height: 900px;
    overflow: hidden;
    background: var(--backdrop);
    font-family: "Montserrat", sans-serif;
  }
  .card {
    position: absolute;
    left: 250px;
    width: 700px;
    height: 400px;
    overflow: hidden;
    box-shadow: 0 6px 18px rgba(0,0,0,0.25);
  }
  .card-front { top: 30px; background: var(--paper); }
  .card-back {
    top: 470px;
    background: linear-gradient(160deg, var(--back-top), var(--back-bottom));
  }
  .brand {
    position: absolute;
    text-align: center;
  }
  .card-front .brand { left: 220px; top: 80px; width: 420px; }
  .brand-name {
    display: block;
    font-weight: 800;
    font-size: 26px;
    letter-spacing: 2px;
    color: var(--ink);
  }
  .brand-tagline {
    display: block;
    margin-top: 6px;
    font-weight: 400;
    font-size: 10.5px;
    letter-spacing: 2.4px;
    color: var(--ink);
    text-transform: uppercase;
  }
  .divider {
    position: absolute;
    left: 40px;
    right: 40px;
    top: 288px;
    height: 1px;
    background: var(--ink);
  }
  .person { position: absolute; left: 40px; top: 230px; }
  .person-name {
    display: block;
    font-weight: 700;
    font-size: 26px;
    color: var(--brand-blue);
  }
  .person-role {
    display: block;
    font-size: 14px;
    color: var(--ink);
    margin-top: 2px;
  }
  .contact { position: absolute; left: 48px; top: 300px; list-style: none; margin: 0; padding: 0; }
  .contact li {
    display: flex;
    align-items: center;
    gap: 12px;
    font-size: 15px;
    color: var(--ink);
    height: 24px;
  }
  .contact svg { width: 14px; height: 14px; fill: var(--brand-blue); }
  .band { position: absolute; left: 0; top: 0; }
  .website {
    position: absolute;
    right: 30px;
    top: 352px;
    font-size: 15px;
    color: var(--paper);
    letter-spacing: 0.5px;
  }
  .card-back .brand { left: 0; width: 700px; top: 165px; }
  .card-back .brand-name { font-size: 38px; color: var(--back-mark); letter-spacing: 3px; }
  .card-back .brand-tagline { font-size: 14px; color: var(--back-mark); letter-spacing: 3.5px; opacity: 0.85; }
</style>
</head>
<body>
  <section class="card card-front">
    <div class="brand">
      <span class="brand-name">MARLOWE CREST GROUP</span>
      <span class="brand-tagline">Clear Water Care From Every Angle</span>
    </div>

    <div class="person">
      <span class="person-name">Darren Holt</span>
      <span class="person-role">owner</span>
    </div>

    <div class="divider"></div>

    <ul class="contact">
      <li>
        <svg viewBox="0 0 24 24" aria-hidden="true"><path d="M6.6 10.8a15.1 15.1 0 0 0 6.6 6.6l2.2-2.2a1 1 0 0 1 1-.25 11.4 11.4 0 0 0 3.6.57 1 1 0 0 1 1 1V20a1 1 0 0 1-1 1A17 17 0 0 1 3 4a1 1 0 0 1 1-1h3.5a1 1 0 0 1 1 1c0 1.25.2 2.45.57 3.6a1 1 0 0 1-.25 1z"/></svg>
        555-014-2236
      </li>
      <li>
        <svg viewBox="0 0 24 24" aria-hidden="true"><path d="M2 5h20v14H2z M2 5l10 8 10-8" fill="var(--brand-blue)" stroke="#fff" stroke-width="1.5"/></svg>
        info@marlowecrestgroup.com
      </li>
    </ul>

    <svg class="band" width="700" height="400" viewBox="0 0 700 400" aria-hidden="true">
      <polygon points="0,370 416,370 410,388 0,388" fill="var(--brand-light)"/>
      <polygon points="0,390 700,390 700,400 0,400" fill="var(--brand-deep)"/>
      <polygon points="428,330 700,330 700,392 414,392" fill="var(--brand-deep)"/>
    </svg>
    <span class="website">www.marlowecrestgroup.com</span>
  </section>

  <section class="card card-back">
    <div class="brand">
      <span class="brand-name">MARLOWE CREST GROUP</span>
      <span class="brand-tagline">Clear Water Care From Every Angle</span>
    </div>
  </section>
</body>
</html>
```